Web Design for Small Healthcare Startup

Hello,

We are seeking a Website Design for a healthcare company focusing on mobile vaccinations, employee health and wellness services onsite at businesses, and consulting services relating to Healthcare Entities in WA state. Our company’s mission is to “To aid in a healthier workplace”. Vitality Caravan will provide on-site wellness services to employers that simplify and streamline employee preventative health as well as onsite consulting services to help with compliance of Healthcare Entities.

We are seeking a Website Design for Vitality Caravan, PLLC. Our company’s mission is to provide mobile health and wellness services to employers onsite at their businesses. These services include mobile vaccinations clinics for employees as well as wellness and health screenings. The company will also offer healtcare compliance consulting services for Healthcare Entities. The company was founded to bring these important healthcare services to businesses and keep employees healthy. Healthy employees are the cornerstone to a great business and we want to help orginazations achieve their goals of having a healthy productive workforce.

We are looking for a moderin website design that will need to be coded. We have attached our current logo design for reference as well as a brief questionare regarding our business for your information (not necessary to include all information). We would like something SEO friendly and easy to navigate.

Thank you!

Vitality Caravan, PLLC

Target Market(s)

Small Businesses

Industry/Entity Type

Healthcare

Coding

Coded - Design and coding required

Number of Pages Required

1 page

Requirements
Nice to have
• SEO Friendly, Incorporate Logo

```html
<!DOCTYPE html>
<html lang="en">
<head>
<meta charset="utf-8">
<title>Vitality Caravan, PLLC — On-Site Mobile Vaccine Clinics</title>
<meta name="description" content="Vitality Caravan provides on-site mobile vaccine clinics and workplace wellness services for employers in WA state.">
<link href="https://fonts.googleapis.com/css2?family=Poppins:wght@400;500;600;700;800&display=swap" rel="stylesheet">
<style>
:root{
  --purple:#7d3b8f;
  --violet:#5b3a98;
  --blue:#2c56a8;
  --magenta:#a63a88;
  --ink:#111111;
  --text:#333333;
  --lavender:#efeaf6;
  --pink:#d3145c;
  --green:#58a72a;
  --plum:#4b2b7a;
  --footer:#0b0b0d;
  --footer-bar:#2a2a2e;
  --grad:linear-gradient(90deg,var(--purple),var(--blue));
}
*{box-sizing:border-box;margin:0;padding:0}
html,body{width:1200px;height:5296px;overflow:hidden}
body{position:relative;font-family:"Poppins",sans-serif;color:var(--text);background:#fff}
.abs{position:absolute}
a{color:inherit;text-decoration:none}
.btn{position:absolute;display:flex;align-items:center;justify-content:center;border-radius:30px;background:var(--grad);color:#fff;font-weight:700;font-size:12px;letter-spacing:.5px;text-transform:uppercase}
.art{position:absolute}
p.body{font-size:12.5px;line-height:21px;color:var(--text)}
h2.title{font-weight:700;color:var(--ink);text-transform:uppercase;font-size:26px;line-height:32px}

/* header */
.brand{position:absolute;left:206px;top:78px;display:flex;align-items:center;gap:10px;color:var(--violet);font-weight:700;font-size:20px;line-height:1}
.brand .dot{width:14px;height:14px;border-radius:50%;background:var(--violet)}
.brand small{display:block;font-size:10px;text-align:right}
.nav{position:absolute;left:440px;top:70px;display:flex;gap:30px;font-size:12px;color:#222}
.hero-blob{position:absolute;right:0;top:0}
.eyebrow{position:absolute;left:210px;top:252px;font-size:26px;font-weight:700;letter-spacing:12px;color:var(--ink)}
.hero-h1{position:absolute;left:210px;top:290px;font-size:44px;line-height:56px;font-weight:800;color:var(--ink);text-transform:uppercase}
.hero-p{position:absolute;left:210px;top:408px;width:400px}

/* purple bands */
.band{position:absolute;left:0;width:1200px}
.band-text{color:#fff}
.band-text h2{color:#fff}
.band-text p{color:#f1eaf7}

/* cards */
.card{position:absolute;width:341px;height:353px;box-shadow:0 8px 24px rgba(60,40,110,.15);background:#fff}
.card .pic{height:185px}
.card h3{margin:30px 26px 8px;font-size:18px;font-weight:700;text-transform:uppercase}
.card p{margin:0 26px;font-size:11.5px;line-height:19px}
.card .more{display:block;margin:14px 26px 0;font-size:11px;font-weight:700}
.card.dark{background:linear-gradient(180deg,var(--purple),var(--blue));color:#fff}
.card.dark p{color:#eee}

/* contact */
.info{position:absolute;left:220px;display:flex;gap:26px;color:#fff}
.info .ico{width:64px;height:64px;border-radius:50%;background:#fff;display:flex;align-items:center;justify-content:center;box-shadow:0 0 0 6px rgba(255,255,255,.25)}
.info h4{font-size:13px;font-weight:700;margin-top:12px}
.info span{font-size:11.5px;line-height:20px;color:#e5dcf0}
.field{position:absolute;height:42px;border-radius:6px;background:#fff;font-size:11.5px;font-style:italic;color:#888;padding:12px 22px}

/* steps */
.step{position:absolute;top:4079px;width:140px;text-align:center}
.step .label{height:37px;background:#fff;font-weight:700;font-size:17px;color:var(--ink);line-height:37px;box-shadow:0 4px 12px rgba(0,0,0,.1)}
.step .box{height:97px;color:#fff;font-size:10.5px;font-weight:700;line-height:14px;padding:14px 14px;text-transform:uppercase;display:flex;align-items:center;justify-content:center}
.step .tip{width:0;height:0;margin:0 auto;border-left:12px solid transparent;border-right:12px solid transparent;border-top:20px solid}

/* footer */
.foot h5{font-size:14px;font-weight:700;color:#fff;margin-bottom:14px}
.foot li{list-style:none;font-size:11.5px;color:#ddd;margin-bottom:12px}
</style>
</head>
<body>

<!-- HEADER / HERO -->
<svg class="hero-blob" width="440" height="420" viewBox="0 0 440 420" aria-hidden="true">
  <defs><linearGradient id="hb" x1="0" y1="0" x2="1" y2="1"><stop offset="0" stop-color="#7d3b8f"/><stop offset="1" stop-color="#3a3fa8"/></linearGradient></defs>
  <path d="M60 0 C120 60 240 40 280 140 C320 240 360 320 440 360 L440 0 Z" fill="url(#hb)"/>
</svg>
<div class="art" role="img" aria-label="Illustration of a smiling doctor surrounded by health icons" style="left:600px;top:144px;width:600px;height:472px;border-radius:50% 40% 20% 50%;background:radial-gradient(circle at 45% 55%,#8b4fc0 0%,#5a3aa2 45%,rgba(90,60,170,0) 72%)"></div>

<a class="brand" href="#"><span class="dot"></span><span>Vitality Caravan<small>PLLC</small></span></a>
<nav class="nav"><a href="#">Home</a><a href="#">About Us</a><a href="#">Services</a><a href="#">Products</a><a href="#">Blogs</a></nav>
<a class="btn" href="#contact" style="left:855px;top:62px;width:135px;height:38px;box-shadow:0 0 0 4px rgba(255,255,255,.3)">Contact Us</a>

<div class="eyebrow">MAKING THE</div>
<h1 class="hero-h1">Workplace a<br>healthier place.</h1>
<p class="body hero-p">Lorem ipsum dolor sit amet, consectetur adipiscing elit, sed do eiusmod tempor incididunt ut labore et dolore magna aliqua.</p>
<a class="btn" href="#" style="left:210px;top:472px;width:137px;height:38px;font-size:11px">Our Products</a>

<!-- SPECIALIZE -->
<div class="art" role="img" aria-label="White mobile clinic van" style="left:0;top:822px;width:575px;height:256px;border-radius:0 90px 40px 0;background:linear-gradient(180deg,#f4f4f6,#c9cacf)"></div>
<div class="art" role="img" aria-label="Second white mobile clinic van" style="left:1038px;top:822px;width:162px;height:256px;border-radius:40px 0 0 40px;background:linear-gradient(180deg,#f4f4f6,#c9cacf)"></div>
<h2 class="title abs" style="left:440px;top:784px;width:550px;text-align:right;font-size:25px;line-height:32px">Vitality Caravan specializes<br>in providing seamless, hassle-free,<br>on-site mobile vaccine clinics.</h2>
<p class="body abs" style="left:580px;top:914px;width:410px;text-align:center">Lorem ipsum dolor sit amet, consectetur adipiscing elit, sed do eiusmod tempor incididunt ut labore et dolore magna aliqua. Quis ipsum suspendisse ultrices gravida. Risus commodo viverra maecenas accumsan lacus vel facilisis. Lorem ipsum dolor sit amet, consectetur adipiscing elit, sed do eiusmod tempor incididunt ut labore et dolore magna aliqua. Quis ipsum suspendisse ultrices gravida. Risus commodo viverra maecenas accumsan lacus.</p>

<!-- NO CROWDED -->
<svg class="band" style="top:1171px" height="473" viewBox="0 0 1200 473" preserveAspectRatio="none" aria-hidden="true">
  <defs><linearGradient id="g1" x1="0" y1="0" x2="1" y2="0"><stop offset="0" stop-color="#7d3b8f"/><stop offset="1" stop-color="#2c56a8"/></linearGradient></defs>
  <path d="M0 40 C300 -10 700 0 1200 45 L1200 440 C800 470 400 470 0 430 Z" fill="url(#g1)"/>
</svg>
<div class="band-text">
  <h2 class="title abs" style="left:210px;top:1290px;width:460px;font-size:25px">No crowded waiting rooms,<br>no long lines, no hassle!</h2>
  <p class="body abs" style="left:210px;top:1376px;width:420px">Lorem ipsum dolor sit amet, consectetur adipiscing elit, sed do eiusmod tempor incididunt ut labore et dolore magna aliqua. Quis ipsum suspendisse ultrices gravida. Risus commodo viverra maecenas accumsan lacus vel facilisis. Lorem ipsum dolor sit amet, consectetur adipiscing elit, sed do eiusmod tempor incididunt ut labore et dolore magna aliqua. Quis ipsum suspendisse ultrices gravida. Risus commodo viverra maecenas accumsan.</p>
</div>
<div class="art" role="img" aria-label="Illustration of a masked man waving away virus particles" style="left:678px;top:1233px;width:350px;height:340px;border-radius:24px;background:linear-gradient(160deg,#ffffff,#dcdfee)"></div>

<!-- WORKPLACE CLINICS -->
<div class="art" role="img" aria-label="Illustration of office employees meeting in a workplace" style="left:164px;top:1705px;width:432px;height:278px;background:linear-gradient(180deg,#f3f3f6,#dfe2ec)"></div>
<h2 class="title abs" style="left:651px;top:1776px;width:420px;font-size:25px">Specializing in workplace<br>employee vaccine clinics.</h2>
<p class="body abs" style="left:651px;top:1852px;width:400px">Lorem ipsum dolor sit amet, consectetur adipiscing elit, sed do eiusmod tempor incididunt ut labore et dolore magna aliqua. Quis ipsum suspendisse ultrices gravida. Risus commodo viverra maecenas accumsan lacus vel facilisis. Lorem ipsum dolor sit amet, consectetur adipiscing elit, sed do eiusmod tempor incididunt ut labore et dolore magna aliqua. Quis ipsum suspendisse ultrices gravida.</p>

<!-- OFFERING -->
<svg class="abs" style="left:0;top:2150px" width="1200" height="760" viewBox="0 0 1200 760" preserveAspectRatio="none" aria-hidden="true">
  <path d="M0 0 L1200 0 L1200 660 C900 740 400 760 0 640 Z" fill="#f5f1fa"/>
</svg>
<h2 class="title abs" style="left:0;top:2300px;width:1200px;text-align:center;font-size:25px">Offering flu and covid vaccinations</h2>
<article class="card dark" style="left:246px;top:2390px">
  <div class="pic" role="img" aria-label="Flu vaccine vial and syringe with shield" style="background:radial-gradient(circle at 50% 45%,#5d7fd0,rgba(0,0,0,0) 60%)"></div>
  <h3>Flu Vaccinations</h3>
  <p>Lorem ipsum dolor sit amet, consectetur adipiscing elit, sed do eiusmod tempornicidi dunt ut labore et dolore magna aliqua.</p>
  <a class="more" href="#">READ MORE</a>
</article>
<article class="card" style="left:598px;top:2390px">
  <div class="pic" role="img" aria-label="Covid vaccine vial and syringe with crossed-out virus" style="background:linear-gradient(90deg,var(--purple),var(--blue))"></div>
  <h3 style="color:var(--ink)">Covid Vaccinations</h3>
  <p>Lorem ipsum dolor sit amet, consectetur adipiscing elit, sed do eiusmod tempornicidi dunt ut labore et dolore magna aliqua.</p>
  <a class="more" href="#" style="color:var(--ink)">READ MORE</a>
</article>

<!-- RESERVE -->
<div class="art" role="img" aria-label="Illustration of a nurse vaccinating a seated patient" style="left:216px;top:3021px;width:308px;height:257px;background:linear-gradient(180deg,#f1f2f7,#dde2f0)"></div>
<h2 class="title abs" style="left:569px;top:2998px;width:460px;font-size:25px">Reserve your on-site mobile<br>vaccine clinic today!</h2>
<p class="body abs" style="left:569px;top:3070px;width:420px">Sed ut perspiciatis unde omnis iste natus error sit voluptatem accusantium doloremque laudantium, totam rem aperiam, eaque ipsa quae ab illo inventore veritatis et quasi architecto beatae vitae dicta sunt explicabo. Nemo enim ipsam voluptatem quia voluptas sit aspernatur aut odit aut fugit, sed quia consequuntur magni dolores eos qui ratione voluptatem sequi nesciunt.</p>
<a class="btn" href="#contact" style="left:569px;top:3218px;width:255px;height:45px;font-size:11px">Available dates/time blocks</a>

<!-- CONTACT -->
<svg class="band" id="contact" style="top:3390px" height="515" viewBox="0 0 1200 515" preserveAspectRatio="none" aria-hidden="true">
  <defs><linearGradient id="g2" x1="0" y1="0" x2="1" y2="0"><stop offset="0" stop-color="#7d3b8f"/><stop offset="1" stop-color="#2c56a8"/></linearGradient></defs>
  <path d="M0 30 C400 -10 800 -10 1200 30 L1200 490 C800 525 400 525 0 490 Z" fill="url(#g2)"/>
</svg>
<h2 class="title abs" style="left:0;top:3434px;width:1200px;text-align:center;color:#fff;font-size:25px">Reserve your on-site mobile<br>vaccine clinic today!</h2>

<div class="info" style="top:3540px">
  <div class="ico"><svg width="22" height="22" viewBox="0 0 24 24"><path d="M12 2a7 7 0 0 0-7 7c0 5 7 13 7 13s7-8 7-13a7 7 0 0 0-7-7zm0 9.5A2.5 2.5 0 1 1 12 6.5a2.5 2.5 0 0 1 0 5z" fill="#5b3a98"/></svg></div>
  <div><h4>OFFICE ADDRESS</h4><span>000 Somewhere Street, Suite 0000<br>Somewhere, AA 00000</span></div>
</div>
<div class="info" style="top:3652px">
  <div class="ico"><svg width="22" height="22" viewBox="0 0 24 24"><path d="M6.6 10.8a15 15 0 0 0 6.6 6.6l2.2-2.2a1 1 0 0 1 1-.25 11 11 0 0 0 3.6.6 1 1 0 0 1 1 1V20a1 1 0 0 1-1 1A17 17 0 0 1 3 4a1 1 0 0 1 1-1h3.5a1 1 0 0 1 1 1c0 1.25.2 2.45.6 3.6a1 1 0 0 1-.25 1z" fill="#5b3a98"/></svg></div>
  <div><h4>PHONE NUMBER</h4><span style="font-size:13px">509-555-0142</span></div>
</div>
<div class="info" style="top:3764px">
  <div class="ico"><svg width="22" height="22" viewBox="0 0 24 24"><path d="M3 5h18v14H3z" fill="#5b3a98"/><path d="M3 6l9 7 9-7" fill="none" stroke="#fff" stroke-width="1.8"/></svg></div>
  <div><h4>EMAIL ADDRESS</h4><span>info@vitalitycaravan.com</span></div>
</div>

<form>
  <div class="field" style="left:577px;top:3541px;width:405px">Business Name...</div>
  <div class="field" style="left:577px;top:3598px;width:193px">location...</div>
  <div class="field" style="left:778px;top:3598px;width:204px">Contact Person Info...</div>
  <div class="field" style="left:577px;top:3656px;width:405px">Anticipated # of employees/vaccines.</div>
  <div class="field" style="left:577px;top:3715px;width:405px">Block of time desired).</div>
  <div class="btn" style="left:577px;top:3775px;width:405px;height:38px;background:#fff;color:var(--ink);font-size:11px">Submit Now</div>
</form>

<!-- STEPS -->
<h2 class="title abs" style="left:0;top:3992px;width:1200px;text-align:center;font-size:25px">Our Steps</h2>
<div class="step" style="left:269px">
  <div class="label">STEPS 1</div>
  <div class="box" style="background:var(--pink)">Submit vaccine clinic needs questionnaire.</div>
  <div class="tip" style="border-top-color:var(--pink)"></div>
</div>
<div class="step" style="left:527px">
  <div class="label">STEPS 1</div>
  <div class="box" style="background:var(--green)">We will contact you to schedule on-site vaccine clinic.</div>
  <div class="tip" style="border-top-color:var(--green)"></div>
</div>
<div class="step" style="left:787px">
  <div class="label">STEPS 1</div>
  <div class="box" style="background:var(--plum)">Prepare your employees for vaccine clinic day.</div>
  <div class="tip" style="border-top-color:var(--plum)"></div>
</div>
<svg class="abs" style="left:200px;top:4255px" width="800" height="80" viewBox="0 0 800 80" aria-hidden="true">
  <path d="M0 30 C100 0 180 60 300 30 S500 0 560 30 S720 60 800 30" fill="none" stroke="#e6e6ea" stroke-width="10" stroke-linecap="round"/>
  <line x1="139" y1="4" x2="139" y2="40" stroke="#d3145c" stroke-dasharray="3 4" stroke-width="2"/>
  <line x1="397" y1="4" x2="397" y2="40" stroke="#58a72a" stroke-dasharray="3 4" stroke-width="2"/>
  <line x1="657" y1="4" x2="657" y2="40" stroke="#4b2b7a" stroke-dasharray="3 4" stroke-width="2"/>
  <circle cx="139" cy="44" r="9" fill="#d3145c"/><circle cx="397" cy="44" r="9" fill="#58a72a"/><circle cx="657" cy="44" r="9" fill="#4b2b7a"/>
</svg>
<a class="btn" href="#" style="left:440px;top:4363px;width:154px;height:45px;font-size:10.5px">Public Health Flu Shot</a>
<a class="btn" href="#" style="left:604px;top:4363px;width:156px;height:45px;font-size:10px;line-height:12px;flex-direction:column"><span style="font-weight:500;letter-spacing:2px;font-size:8.5px">CALL US NOW</span><span>509-555-0142</span></a>

<!-- DOCUMENTS -->
<svg class="abs" style="left:0;top:4520px" width="1200" height="420" viewBox="0 0 1200 420" preserveAspectRatio="none" aria-hidden="true">
  <path d="M0 0 C400 40 800 40 1200 0 L1200 420 L0 420 Z" fill="#f5f1fa"/>
</svg>
<div class="art" role="img" aria-label="Illustration of a shield, syringe, vaccine vial and blue virus particles" style="left:185px;top:4562px;width:401px;height:288px;background:radial-gradient(circle at 45% 50%,#3b6bd6 0%,#6a8fe0 30%,rgba(245,241,250,0) 65%)"></div>
<h2 class="title abs" style="left:625px;top:4632px;font-size:25px">Nora’s documents</h2>
<p class="body abs" style="left:625px;top:4674px;width:370px">Avoid long lines ... Each employee can sign up for specific time or dept managers can release employees in phases to clinic. Also available: book for entire day so employees can get vaccinated as their workload permits. Employees will avoid congested waiting rooms at medical offices and long lines at local pharmacies</p>

<!-- FOOTER -->
<svg class="abs" style="left:0;top:4880px" width="1200" height="416" viewBox="0 0 1200 416" preserveAspectRatio="none" aria-hidden="true">
  <path d="M0 60 C400 0 800 0 1200 60 L1200 416 L0 416 Z" fill="#0b0b0d"/>
</svg>
<footer class="foot">
  <div class="brand" style="left:210px;top:5003px;color:#fff"><span class="dot" style="background:#fff"></span><span>Vitality Caravan<small>PLLC</small></span></div>
  <p class="abs" style="left:210px;top:5106px;width:230px;font-size:11.5px;line-height:21px;color:#ddd">Lorem ipsum dolor sit amet, consectetur adipiscing elit, sed do eiusmod tempor incididunt ut labore et dolore magna aliqua.</p>
  <div class="abs" style="left:501px;top:5056px"><h5>Quicks Links</h5><ul><li>Home</li><li>About Us</li><li>Products</li><li>vaccine</li><li>Questions</li></ul></div>
  <div class="abs" style="left:653px;top:5056px"><h5>Resources</h5><ul><li>Blog</li><li>About</li><li>Contact</li><li>Terms</li></ul></div>
  <div class="abs" style="left:820px;top:5056px"><h5>Contact Us</h5>
    <div style="display:flex;gap:12px;align-items:center;color:#ddd;font-size:11.5px;line-height:14px;margin-bottom:18px"><span style="width:24px;height:24px;border-radius:50%;background:var(--violet);display:inline-block"></span>0000 somewhere st.<br>000 somewhere</div>
    <div style="display:flex;gap:12px;align-items:center;color:#ddd;font-size:11.5px"><span style="width:24px;height:24px;border-radius:50%;background:var(--violet);display:inline-block"></span>509-555-0142</div>
  </div>
  <div class="abs" style="left:0;top:5252px;width:1200px;height:44px;background:var(--footer-bar);color:#fff;font-size:10.5px;font-weight:600;display:flex;align-items:center;justify-content:center">COPYRIGHT © VITALITY CARAVAN. ALL RIGHTS RESERVED.</div>
</footer>

</body>
</html>
```